Independent International Travel Romantic Comedy Film Poster Design

We need a fun, eye-catching film poster for a romantic comedy shot in San Francisco and throughout the country of Anatolia. Very open to cute ideas that grab attention as a small thumbnail.

If your design includes photos and is chosen we would like to take photos of our actors in similar position to replace for your final delivery.

Story: A girl books a trip with her boyfriend, but when he breaks up with her, she is stuck with One-Way Detour tickets in his name. Her friends convince her to find a guy with her ex-boyfriend's name to still go on the trip.

Our film trailer for ideas: https://www.reelhopper.net/watch?v=7Qp4LmN2zRx

Our temp website for ideas: http://www.OneWayDetourFilm.com

Target Market(s)

Young Travelers, Independent Film Lovers, Millennials, 90's RomCom Fans, The Marnie Colter Journals fans

Industry/Entity Type

Travel

Requirements
Must have
• We really want the poster thumbnail to stand out when seen with other independent films on Streamlark.com/ondemand
Nice to have
• Some of our ideas include a "pop-up book map" with characters and iconic landmarks. We like posters for movies like Velvet Errand (pink version), Quietly Tangled, Woman Near the Ferry, Watch Lark Hum, Twelve Rainy Tuesdays, Tide Nine...

```html
<!DOCTYPE html>
<html lang="en">
<head>
<meta charset="utf-8">
<title>One-Way Detour — Film Poster</title>
<link href="https://fonts.googleapis.com/css2?family=Barlow+Condensed:wght@500;600&family=Montserrat:ital,wght@0,500;1,900&family=Playfair+Display:ital@1&display=swap" rel="stylesheet">
<style>
  :root {
    --sky-top: #a4dbd8;
    --sky-mid: #dcea9a;
    --sun-yellow: #f6e66a;
    --sun-core: #fffdf2;
    --ink: #111111;
    --band: #000000;
    --paper: #ffffff;
    --title-shadow: rgba(150, 130, 40, 0.35);
  }
  * { margin: 0; padding: 0; box-sizing: border-box; }
  html, body { width: 800px; height: 1200px; overflow: hidden; background: #d9d9d9; }
  .poster {
    position: relative;
    width: 800px;
    height: 1200px;
    overflow: hidden;
    background:
      radial-gradient(ellipse 330px 300px at 50% 63%, var(--sun-core) 0%, #fbf3a8 22%, var(--sun-yellow) 55%, rgba(246,230,106,0) 100%),
      linear-gradient(to bottom, var(--sky-top) 0%, var(--sky-mid) 30%, var(--sun-yellow) 55%, var(--sun-yellow) 100%);
  }
  .cast-top {
    position: absolute; top: 40px; left: 0; width: 100%;
    display: flex; justify-content: space-between; padding: 0 82px 0 80px;
    font-family: "Barlow Condensed", sans-serif; font-weight: 500;
    font-size: 27px; color: var(--paper); letter-spacing: 0.2px;
  }
  .plane {
    position: absolute; left: 233px; top: 172px; width: 282px; height: 92px;
  }
  .director-credit {
    position: absolute; top: 318px; left: 0; width: 100%; text-align: center;
    font-family: "Montserrat", sans-serif; font-weight: 500;
    font-size: 17px; letter-spacing: 9px; color: var(--ink);
    padding-left: 10px;
  }
  .title {
    position: absolute; top: 370px; left: 0; width: 100%; text-align: center;
    color: var(--paper); white-space: nowrap;
    text-shadow: 0 0 18px var(--title-shadow);
  }
  .title-small {
    font-family: "Playfair Display", serif; font-style: italic;
    font-size: 50px; margin-right: 14px;
  }
  .title-main {
    font-family: "Montserrat", sans-serif; font-style: italic; font-weight: 900;
    font-size: 66px; letter-spacing: 0.5px;
  }
  .figures {
    position: absolute; left: 252px; top: 512px; width: 300px; height: 456px;
  }
  .billing-band {
    position: absolute; left: 0; top: 967px; width: 100%; height: 233px;
    background: var(--band); color: var(--paper);
    font-family: "Barlow Condensed", sans-serif; font-weight: 500;
    text-align: center;
  }
  .billing-line {
    display: flex; justify-content: center; align-items: baseline; gap: 14px;
    font-size: 19px; line-height: 1;
  }
  .billing-line.l1 { margin-top: 21px; }
  .billing-line.l2, .billing-line.l3 { margin-top: 9px; }
  .billing-line.l4 { margin-top: 10px; font-size: 22px; }
  .role {
    display: inline-block; font-size: 6px; line-height: 1.05; text-align: right;
    margin-right: 4px; vertical-align: middle;
  }
  .sponsor-main {
    margin-top: 9px; display: inline-flex; align-items: center; gap: 6px;
    font-weight: 600; font-size: 13px; letter-spacing: 0.5px;
  }
  .sponsor-main .dot { width: 16px; height: 16px; border: 1.5px solid var(--paper); border-radius: 50%; }
  .sponsor-row {
    margin-top: 10px; display: flex; justify-content: center; align-items: center; gap: 22px;
    font-size: 10px; letter-spacing: 0.5px;
  }
  .badge-row {
    margin-top: 10px; display: flex; justify-content: center; align-items: center; gap: 12px;
  }
  .badge { width: 16px; height: 7px; background: #bdbdbd; border-radius: 2px; }
  .badge.wide { width: 26px; }
</style>
</head>
<body>
<main class="poster">
  <div class="cast-top">
    <span>HARRIET VANCE</span>
    <span>DELIA OKAFOR</span>
    <span>MINA ROE</span>
  </div>

  <svg class="plane" role="img" aria-label="Passenger jet airliner flying across the sky" viewBox="0 0 282 92">
    <defs>
      <linearGradient id="planeTone" x1="0" y1="0" x2="1" y2="1">
        <stop offset="0" stop-color="#8a3a3a" stop-opacity="0.35"/>
        <stop offset="1" stop-color="#6d6d6d" stop-opacity="0.35"/>
      </linearGradient>
    </defs>
    <rect x="0" y="0" width="282" height="92" rx="10" fill="url(#planeTone)"/>
  </svg>

  <div class="director-credit">ROWAN TELLIS</div>

  <h1 class="title"><span class="title-small">one-way</span><span class="title-main">DETOUR</span></h1>

  <svg class="figures" role="img" aria-label="Silhouettes of a woman and a man standing side by side facing the sunset" viewBox="0 0 300 456">
    <defs>
      <linearGradient id="figureTone" x1="0" y1="0" x2="0" y2="1">
        <stop offset="0" stop-color="#2a2a1c" stop-opacity="0.25"/>
        <stop offset="1" stop-color="#1a1a12" stop-opacity="0.55"/>
      </linearGradient>
    </defs>
    <rect x="0" y="0" width="300" height="456" rx="12" fill="url(#figureTone)"/>
  </svg>

  <section class="billing-band">
    <div class="billing-line l1">
      <span>THE LANTERN COLLECTIVE</span>
      <span><span class="role">PRESENTS IN<br>ASSOCIATION WITH</span>MERIDIAN SKYWAYS &amp; AZURE TOURISM “ONE-WAY DETOUR”</span>
    </div>
    <div class="billing-line l2">
      <span>HARRIET VANCE</span><span>DELIA OKAFOR</span><span>MINA ROE</span><span>JULIAN TEODOR MARSH</span>
    </div>
    <div class="billing-line l3">
      <span><span class="role">CASTING<br>BY</span>PRIYA LUND CASTELL</span>
      <span><span class="role">DIRECTOR OF<br>PHOTOGRAPHY</span>EMMET SARKIS</span>
      <span><span class="role">MUSIC<br>BY</span>CASPIAN HALE</span>
      <span><span class="role">EDITED<br>BY</span>LEON FARROW</span>
    </div>
    <div class="billing-line l4">
      <span><span class="role">WRITTEN AND<br>DIRECTED BY</span>ROWAN TELLIS</span>
    </div>
    <div class="sponsor-main"><span>MERIDIAN SKYWAYS</span><span class="dot"></span></div>
    <div class="sponsor-row">
      <span>AZURE</span><span>ANATOLIA</span><span>KESTREL HOTELS</span>
    </div>
    <div class="badge-row">
      <span class="badge"></span><span class="badge"></span><span class="badge"></span>
      <span class="badge wide"></span><span style="font-size:9px">BRIGHTLINK</span>
    </div>
  </section>
</main>
</body>
</html>
```